Gardening and life coaching business card design

I need business cards for a new company in the heart of the Ozarks at the Lake of the Ozarks. Tallow Brook Harvest's mission is to teach the world to fish. We provide fresh local fish and produce using permaculture methods. We work with nature and the flow to create more harmony and less impact. We also coach others who are ready to make this transition. We specialize in microgreens and Aquaculture systems. I would like to make Tallow Brook Harvest come alive with green vines and purple flowers I wold like Tallow Brook Harvest to be in green and the rest of the lettering to be in purple. The feel of the card should be that of the Garden of Eden.

Industry/Entity Type

Life Coaching

Contact Information for Business Card

Tallow Brook Harvest
Owner/Operator Marisol Pettigrew
Contact Info:
(555) 214-9083
tallowbrookharvest.example
tallowbrookharvest is also on FB

```html
<!DOCTYPE html>
<html lang="en">
<head>
<meta charset="utf-8">
<title>Tallow Brook Harvest — Business Card</title>
<link href="https://fonts.googleapis.com/css2?family=Ubuntu:wght@400;500&family=Raleway:wght@300;400;700&display=swap" rel="stylesheet">
<style>
  :root {
    --canvas-bg: #e9e7e2;
    --card-white: #ffffff;
    --card-shade: #e6e6e6;
    --brand-green: #1f6a30;
    --green-light: #2f8a43;
    --green-dark: #1a5a28;
    --divider-grey: #a9a9a9;
    --ink-light: #ffffff;
  }
  * { margin: 0; padding: 0; box-sizing: border-box; }
  html, body { width: 1200px; height: 858px; overflow: hidden; }
  body {
    background: var(--canvas-bg);
    display: flex;
    align-items: center;
    justify-content: center;
    gap: 40px;
  }
  .card {
    position: relative;
    width: 560px;
    height: 320px;
    background: var(--card-white);
    overflow: hidden;
    box-shadow: 0 2px 8px rgba(0,0,0,0.12);
  }
  .card-front .panel-art {
    position: absolute;
    inset: 0;
    width: 100%;
    height: 100%;
  }
  .brand-block {
    position: absolute;
    left: 30px;
    bottom: 34px;
    width: 220px;
  }
  .brand-name {
    font-family: "Ubuntu", sans-serif;
    font-weight: 500;
    font-size: 38px;
    line-height: 1.02;
    color: var(--brand-green);
  }
  .contact-block {
    position: absolute;
    left: 340px;
    top: 34px;
    color: var(--ink-light);
    font-family: "Raleway", sans-serif;
  }
  .person-name { font-weight: 700; font-size: 22px; letter-spacing: 0.2px; }
  .person-role { font-weight: 400; font-size: 16px; margin-top: 2px; }
  .address { font-weight: 300; font-size: 13px; line-height: 1.45; margin-top: 26px; }
  .links { list-style: none; margin-top: 22px; font-weight: 300; font-size: 13px; }
  .links li { display: flex; align-items: center; gap: 8px; line-height: 1.55; }
  .links .marker {
    width: 13px; height: 13px;
    background: var(--ink-light);
    border-radius: 2px;
    flex: none;
  }
  .card-back {
    background: linear-gradient(160deg, var(--card-white) 30%, var(--card-shade) 100%);
    display: flex;
    align-items: center;
    justify-content: center;
  }
  .back-name {
    font-family: "Ubuntu", sans-serif;
    font-weight: 400;
    font-size: 40px;
    color: var(--brand-green);
  }
</style>
</head>
<body>
  <section class="card card-front" aria-label="Business card front">
    <svg class="panel-art" viewBox="0 0 560 320" preserveAspectRatio="none" aria-hidden="true">
      <defs>
        <linearGradient id="greenFill" x1="0" y1="0" x2="1" y2="1">
          <stop offset="0" stop-color="var(--green-dark)"/>
          <stop offset="0.5" stop-color="var(--green-light)"/>
          <stop offset="1" stop-color="var(--green-dark)"/>
        </linearGradient>
      </defs>
      <path d="M262 0 Q296 160 318 320 L560 320 L560 0 Z" fill="var(--divider-grey)"/>
      <path d="M274 0 Q308 160 330 320 L560 320 L560 0 Z" fill="url(#greenFill)"/>
    </svg>
    <div class="brand-block">
      <p class="brand-name">Tallow<br>Brook<br>Harvest</p>
    </div>
    <div class="contact-block">
      <p class="person-name">Marisol Pettigrew</p>
      <p class="person-role">Owner/Operator</p>
      <p class="address">42 Larkspur Ln. Unit 9<br>Fernhollow, Missouri</p>
      <ul class="links">
        <li><span class="marker"></span>(555) 214-9083</li>
        <li><span class="marker"></span>tallowbrookharvest.example</li>
        <li><span class="marker"></span>tallowbrookharvest</li>
      </ul>
    </div>
  </section>

  <section class="card card-back" aria-label="Business card back">
    <p class="back-name">Tallow Brook Harvest</p>
  </section>
</body>
</html>
```